Onboarding Carousel UI/UX design

We need a great UI/UX design for our onboarding carousel as attached in the PDF document. The chosen designers will be given our brand book with colors and styles to be used. The images must be focused on the content of each slide and be professional unique style (Do not use the childish cartoons we have used for placeholders)

Industry/Entity Type

Mortgage Brokerage

Number of Pages Required

5+ page

Other font styles liked:
• Roboto

Requirements
Must have
• Great UI / UX design
Very relevant content of the images to match the slide
Nice to have
• Brand book

https://proto.velmarink.com/view/a4c7e210-8b3f-4d19-a6e2-5f0c91b7d3e8-c2fa/?fullscreen

Image styles we like. Would need to be customized and made unique for us.

https://pixelmarsh.com/shots/4817302-Tarvo-Quillnet-Illustration-Collaboration
https://brackwellstudio.co.za/software-client-style-frames
Should not have
• Do not use the childish images we have used as placeholders

```html
<!DOCTYPE html>
<html lang="en">
<head>
<meta charset="utf-8">
<title>Onboarding – Create your profile</title>
<link href="https://fonts.googleapis.com/css2?family=Roboto:wght@300;400;700&display=swap" rel="stylesheet">
<style>
  :root {
    --page: #ffffff;
    --screen: #f7f2f1;
    --ink: #111111;
    --muted: #7a7a7a;
    --accent: #0d96e6;
    --orange: #f5a000;
    --orange-soft: #fbd98f;
    --green-soft: #cfe5c4;
    --blue-soft: #c6e3f6;
    --dot-line: #222222;
  }
  * { margin: 0; padding: 0; box-sizing: border-box; }
  html, body {
    width: 1200px;
    height: 2598px;
    overflow: hidden;
    background: var(--page);
    font-family: "Roboto", sans-serif;
  }
  .screen {
    position: relative;
    width: 1200px;
    height: 2598px;
    background: var(--screen);
    border-radius: 96px;
    overflow: hidden;
  }
  .screen-title {
    position: absolute;
    left: 115px;
    top: 250px;
    width: 900px;
    font-size: 83px;
    line-height: 112px;
    font-weight: 700;
    color: var(--ink);
    letter-spacing: -0.5px;
  }
  .hero-illustration {
    position: absolute;
    left: 112px;
    top: 730px;
    width: 976px;
    height: 856px;
    border-radius: 24px;
    background:
      radial-gradient(circle at 22% 18%, var(--blue-soft) 0%, rgba(198,227,246,0) 32%),
      radial-gradient(circle at 14% 30%, var(--green-soft) 0%, rgba(207,229,196,0) 26%),
      radial-gradient(ellipse at 66% 78%, var(--orange) 0%, var(--orange-soft) 34%, rgba(251,217,143,0) 62%),
      linear-gradient(180deg, var(--screen) 0%, #f9ece0 100%);
  }
  .screen-lead {
    position: absolute;
    left: 0;
    top: 1705px;
    width: 1200px;
    text-align: center;
    font-size: 55px;
    line-height: 77px;
    font-weight: 400;
    color: var(--ink);
  }
  .screen-note {
    position: absolute;
    left: 0;
    top: 1978px;
    width: 1200px;
    text-align: center;
    font-size: 38px;
    line-height: 61px;
    font-weight: 300;
    color: var(--muted);
  }
  .carousel-nav {
    position: absolute;
    left: 0;
    top: 2330px;
    width: 1200px;
    height: 130px;
  }
</style>
</head>
<body>
  <main class="screen">
    <h1 class="screen-title">Create your profile<br>data for the<br>application</h1>

    <div class="hero-illustration" role="img" aria-label="Line illustration of a mortgage applicant in an orange jacket entering employment, income, assets and liabilities on a laptop, beside a ring of four coloured circles representing the profile sections"></div>

    <p class="screen-lead">Tell us about your current<br>situation including employment,<br>income, assets and liabilities</p>

    <p class="screen-note">It is essential to have everything as<br>accurate as possible so you can be<br>presented with the right offers</p>

    <nav class="carousel-nav" aria-label="Onboarding progress">
      <svg width="1200" height="130" viewBox="0 0 1200 130">
        <g fill="none" stroke="var(--dot-line)" stroke-width="4">
          <circle cx="291" cy="64" r="19"/>
          <circle cx="394" cy="64" r="19"/>
          <circle cx="496" cy="64" r="19"/>
          <circle cx="598" cy="64" r="19"/>
          <circle cx="701" cy="64" r="19" fill="var(--accent)"/>
          <circle cx="803" cy="64" r="19"/>
          <circle cx="906" cy="64" r="19"/>
        </g>
        <g class="next-arrow" fill="none" stroke="var(--accent)" stroke-width="13" stroke-linecap="square" stroke-linejoin="miter">
          <polyline points="1005,26 1042,64 1005,102"/>
          <polyline points="1045,26 1082,64 1045,102"/>
        </g>
      </svg>
    </nav>
  </main>
</body>
</html>
```